business card letterhead envelope
Darren Holcomb Realtors
Project: business card letterhead envelope
business card letterhead envelope - Real Estate
Creative Brief
Professional
Darren Holcomb
Attorney/Broker
2817 W. Larkspur Ave Suite B7 Odessa, TX 79748
Darren@PecosPrairieHouses.com
PecosPrairieHouses.com

```html
<!DOCTYPE html>
<html lang="en">
<head>
<meta charset="utf-8">
<title>Darren Holcomb Realtors – Business Card</title>
<link rel="stylesheet" href="https://fonts.googleapis.com/css2?family=Michroma&display=swap">
<style>
  :root {
    --page: #ffffff;
    --card-light: #2ea6e6;
    --card-mid: #1f86d0;
    --card-dark: #1d3c97;
    --ink-navy: #14207a;
    --ink-white: #ffffff;
    --motif-glow: rgba(255, 255, 255, 0.30);
    --motif-fade: rgba(255, 255, 255, 0);
  }
  html, body {
    margin: 0;
    padding: 0;
    width: 1200px;
    height: 688px;
    overflow: hidden;
    background: var(--page);
  }
  .card {
    position: relative;
    width: 1200px;
    height: 688px;
    border-radius: 26px;
    overflow: hidden;
    background: linear-gradient(100deg, var(--card-light) 0%, var(--card-mid) 45%, var(--card-dark) 100%);
    font-family: "Michroma", "Arial", sans-serif;
    color: var(--ink-navy);
  }
  .house-motif {
    position: absolute;
    left: 640px;
    top: 40px;
    width: 540px;
    height: 600px;
    border-radius: 50%;
    background: radial-gradient(ellipse at 50% 45%, var(--motif-glow) 0%, var(--motif-fade) 70%);
  }
  .brand-title {
    position: absolute;
    left: 20px;
    top: 16px;
    margin: 0;
    font-size: 33px;
    font-weight: 400;
    letter-spacing: 1px;
    line-height: 40px;
    text-transform: uppercase;
    color: var(--ink-navy);
    white-space: nowrap;
  }
  .person-name {
    position: absolute;
    left: 44px;
    top: 100px;
    margin: 0;
    font-size: 29px;
    font-weight: 400;
    line-height: 40px;
    text-transform: uppercase;
    color: var(--ink-white);
    white-space: nowrap;
  }
  .person-role {
    position: absolute;
    left: 44px;
    top: 160px;
    margin: 0;
    font-size: 17px;
    line-height: 26px;
    letter-spacing: 1px;
    text-transform: uppercase;
    color: var(--ink-navy);
    white-space: nowrap;
  }
  .contact {
    position: absolute;
    left: 0;
    top: 0;
    font-size: 13px;
    line-height: 22px;
    text-transform: uppercase;
    color: var(--ink-navy);
  }
  .contact__row {
    position: absolute;
    white-space: nowrap;
  }
  .contact__label,
  .contact__value {
    position: absolute;
    top: 0;
    white-space: nowrap;
  }
</style>
</head>
<body>
<div class="card">
  <div class="house-motif" role="img" aria-label="Stylised house roof and shooting star artwork in white"></div>

  <h1 class="brand-title">Darren Holcomb Realtors</h1>
  <h2 class="person-name">Darren Holcomb</h2>
  <p class="person-role">Attorney/Broker</p>

  <div class="contact">
    <div class="contact__row" style="left:18px; top:406px;">
      <span class="contact__label" style="left:0;">Address :</span>
      <span class="contact__value" style="left:116px;">2817 W. Larkspur Ave Suite B7</span>
    </div>
    <div class="contact__row" style="left:18px; top:428px;">
      <span class="contact__value" style="left:116px;">Odessa, TX 79748</span>
    </div>
    <div class="contact__row" style="left:18px; top:450px;">
      <span class="contact__label" style="left:116px;">Phone:</span>
      <span class="contact__value" style="left:196px;">432.555.0148</span>
    </div>
    <div class="contact__row" style="left:18px; top:474px;">
      <span class="contact__label" style="left:116px;">Cell:</span>
      <span class="contact__value" style="left:212px;">432.555.0193</span>
    </div>
    <div class="contact__row" style="left:18px; top:498px;">
      <span class="contact__label" style="left:116px;">Fax:</span>
      <span class="contact__value" style="left:212px;">432.555.0172</span>
    </div>
    <div class="contact__row" style="left:28px; top:532px;">
      <span class="contact__label" style="left:0;">Email: Darren@PecosPrairieHouses.com</span>
    </div>
    <div class="contact__row" style="left:18px; top:556px;">
      <span class="contact__label" style="left:0;">Web Address: PecosPrairieHouses.com</span>
    </div>
  </div>
</div>
</body>
</html>
```